Child Sponsorship Charity Needs a Wordpress Design

BrightPath INTERNATIONAL is a not-for-profit organization that breaks the cycle of poverty through child sponsorship. We work in 7 countries around the world and are based in Canada. We currently have a Wordpress website and want to update the look and create a more engaging user experience. Our donor base is across Canada and our partners work across the globe. PLEASE SEE THE DESIGN BRIEF ATTACHED. We are looking for out site to be clean, colourful, and inviting. It should maintain our brand image, be welcoming to potential donors, and a great resource to current donors.
Updates

Project Deadline Extended Reason: Our Board of Directors wants a chance to provide feedback on the submissions and so we are extending the deadline to give them the opportunity to share their insights. Added Saturday, February 21, 2015

Industry/Entity Type

Charity

Font styles to use
Other font styles liked:
• Helvetica / Helvetica Neue

Requirements
Must have
• Got a list of colours from the designer who made our logo:
• Brightpath Navy blue
• C: 100
• M: 80
• Y: 0
• K: 23
• Or
• R: 2
• G: 60
• B: 132
• Brightpath lighter blue
• C: 34
• M: 0
• Y: 3
• K: 0
• Or
• R: 161
• G: 221
• B: 241
• Brightpath deep red (newsletter accent colour)
• C: 0
• M: 91
• Y: 88
• K: 30
• Or
• R: 178
• G: 44
• B: 34

```html
<!DOCTYPE html>
<html lang="en">
<head>
<meta charset="utf-8">
<title>BrightPath INTERNATIONAL</title>
<link href="https://fonts.googleapis.com/css2?family=Open+Sans:wght@400;600;700&display=swap" rel="stylesheet">
<style>
:root{
  --blue:#1f5ba3;
  --blue-dark:#184b88;
  --navy:#023c84;
  --sky:#a1ddf1;
  --red:#b22c22;
  --orange:#f7941d;
  --dark:#2d2d2d;
  --darker:#232323;
  --text:#666;
  --line:#e3e3e3;
  --page:#ececec;
}
*{box-sizing:border-box;margin:0;padding:0}
html,body{width:864px;height:1200px;overflow:hidden}
body{background:var(--page);font-family:"Open Sans",Helvetica,Arial,sans-serif;color:var(--text);position:relative}
.sheet{position:absolute;left:117px;top:0;width:632px;height:1200px;background:#fff}
.abs{position:absolute}
.brand{left:132px;top:22px;display:flex;align-items:center;gap:6px}
.brand-dot{width:26px;height:26px;border-radius:50%;background:var(--blue)}
.brand-name{font-size:13px;color:var(--navy);font-weight:400}
.call{left:431px;top:25px;display:flex;align-items:center;gap:6px;font-size:8px;color:#555}
.call-icon{width:25px;height:25px;border-radius:50%;background:var(--orange);display:flex;align-items:center;justify-content:center}
.search{left:573px;top:29px;width:159px;height:21px;border:1px solid #ccc;font-size:7.5px;color:#777;padding:5px 8px;display:flex;justify-content:space-between;align-items:center}
.nav{left:130px;top:74px;width:604px;height:37px;background:var(--blue);display:flex;align-items:center}
.nav-home{width:33px;height:37px;background:var(--blue-dark);display:flex;align-items:center;justify-content:center}
.nav a{color:#fff;text-decoration:none;font-size:7.5px;font-weight:600;margin-left:25px;letter-spacing:.1px}
.nav a:first-of-type{margin-left:21px}
.hero{left:130px;top:111px;width:604px;height:246px;background:linear-gradient(100deg,#c44a1c 0%,#d9763a 35%,#8a4a2c 70%,#4a2a1c 100%)}
.hero-title{left:146px;top:275px;font-size:18px;font-weight:700;color:#fff}
.hero-sub{left:146px;top:302px;font-size:11px;font-weight:600;color:#fff;line-height:18.5px}
.hero-arrows{left:691px;top:333px;display:flex;gap:2px}
.hero-arrows span{width:18px;height:18px;background:rgba(0,0,0,.35);display:flex;align-items:center;justify-content:center}
.feature{top:357px;height:80px;width:302px;display:flex}
.feature-icon{width:77px;height:80px;display:flex;align-items:center;justify-content:center}
.feature-body{padding:16px 0 0 20px;color:#fff}
.feature-body h2{font-size:12.5px;font-weight:700;margin-bottom:5px}
.feature-body p{font-size:7px;line-height:15px}
.video{left:130px;top:457px;width:252px;height:181px;background:linear-gradient(160deg,#8a8a80,#b7a991 50%,#6f6a5c)}
.video-bar{position:absolute;left:0;bottom:0;width:100%;height:14px;background:#111;font-size:6px;color:#ddd;padding:3px 0 0 38px}
.play{position:absolute;left:108px;top:72px;width:36px;height:36px;border-radius:50%;background:rgba(0,0,0,.45);border:2px solid #fff;display:flex;align-items:center;justify-content:center}
.welcome h1{position:absolute;left:415px;top:458px;font-size:13.5px;line-height:19px;color:var(--blue);font-weight:700}
.welcome p{position:absolute;left:415px;top:502px;width:316px;font-size:7.5px;line-height:16px}
.btn{background:var(--blue);color:#fff;font-size:7.5px;display:flex;align-items:center;justify-content:center}
.btn-lg{left:416px;top:607px;width:121px;height:31px;font-size:8px}
.section-title{left:130px;top:661px;font-size:10.5px;font-weight:700;color:var(--blue)}
.pager{left:714px;top:667px;display:flex;gap:2px}
.pager span{width:9px;height:9px;border-radius:50%;background:#ccc}
.post{top:690px;width:136px}
.post-img{height:92px}
.post h3{font-size:7px;font-weight:700;color:var(--blue);margin-top:9px}
.post small{display:block;font-size:7px;margin-top:5px}
.divider{left:130px;top:838px;width:604px;height:1px;background:var(--line)}
.card{top:862px;width:188px;height:238px;background:#f8f8f8;border:1px solid #eee}
.card-img{height:114px}
.card h3{font-size:10px;font-weight:700;color:var(--blue);margin:20px 0 0 14px}
.card p{font-size:7.5px;line-height:15px;margin:5px 14px 0}
.card .btn{width:69px;height:21px;margin:10px 0 0 14px}
.footer{left:130px;top:1116px;width:604px;height:70px;background:#f8f8f8;border:1px solid #eee;font-size:7.5px;padding:18px 0 0 20px;line-height:19.5px}
.social{left:620px;top:1142px;display:flex;gap:4px}
.social span{width:22px;height:22px;border-radius:50%}
</style>
</head>
<body>
<div class="sheet"></div>

<div class="abs brand"><span class="brand-dot"></span><span class="brand-name">BrightPath INTERNATIONAL</span></div>

<div class="abs call"><span class="call-icon"><svg width="11" height="11" viewBox="0 0 24 24"><path fill="#fff" d="M6.6 10.8a15.1 15.1 0 0 0 6.6 6.6l2.2-2.2a1 1 0 0 1 1-.25 11.4 11.4 0 0 0 3.6.57 1 1 0 0 1 1 1V20a1 1 0 0 1-1 1A17 17 0 0 1 3 4a1 1 0 0 1 1-1h3.5a1 1 0 0 1 1 1c0 1.25.2 2.45.57 3.57a1 1 0 0 1-.25 1z"/></svg></span>Call us : 555-010-4821</div>

<div class="abs search"><span>Search :</span><svg width="8" height="8" viewBox="0 0 10 10"><circle cx="4" cy="4" r="3" fill="none" stroke="#666" stroke-width="1.3"/><path d="M6.3 6.3 9 9" stroke="#666" stroke-width="1.3"/></svg></div>

<nav class="abs nav">
  <span class="nav-home"><svg width="9" height="8" viewBox="0 0 10 9"><path fill="#fff" d="M5 0 0 4.5h1.3V9h2.7V6h2v3h2.7V4.5H10z"/></svg></span>
  <a>SPONSOR A CHILD</a><a>ABOUT US</a><a>WHERE WE WORK</a><a>PROGRAMS</a><a>GET INVOLVED</a><a>DONATE</a><a>BLOG</a><a>CONTACT</a>
</nav>

<div class="abs hero" role="img" aria-label="Photo of smiling children"></div>
<div class="abs hero-title">OUR FOUNDED IN 1979</div>
<div class="abs hero-sub">BRIGHTPATH INTERNATIONAL IS DEDICATED TO<br>BREAKING THE CYCLE OF POVERTY</div>
<div class="abs hero-arrows"><span><svg width="6" height="8"><path d="M5 1 1 4l4 3" stroke="#ddd" fill="none"/></svg></span><span><svg width="6" height="8"><path d="M1 1l4 3-4 3" stroke="#ddd" fill="none"/></svg></span></div>

<div class="abs feature" style="left:130px;background:var(--blue)">
  <div class="feature-icon" style="background:var(--blue-dark)"><svg width="46" height="40" viewBox="0 0 24 22"><path fill="#fff" d="M12 21 2.5 11.5A5.5 5.5 0 0 1 12 4a5.5 5.5 0 0 1 9.5 7.5z"/></svg></div>
  <div class="feature-body"><h2>SPONSOR A CHILD</h2><p>SPONSORING A CHILD THROUGH BRIGHTPATH<br>INTERNATIONAL ENABLES US...</p></div>
</div>
<div class="abs feature" style="left:432px;background:var(--dark)">
  <div class="feature-icon" style="background:var(--darker)"><svg width="34" height="44" viewBox="0 0 20 26"><path fill="none" stroke="#fff" stroke-width="2" stroke-linecap="round" d="M6 14V4M9 13V2M12 13V3M15 14V6M6 14c-2-2-4-2-4 0l4 7c1 2 3 3 5 3h1c2 0 4-2 4-5v-5"/></svg></div>
  <div class="feature-body"><h2>WHERE WE WORK</h2><p>SPONSORING A CHILD THROUGH BRIGHTPATH<br>INTERNATIONAL ENABLES US...</p></div>
</div>

<div class="abs video" role="img" aria-label="Video still of children standing on a village street">
  <span class="play"><svg width="12" height="12"><path d="M3 1l8 5-8 5z" fill="#fff"/></svg></span>
  <div class="video-bar">0:04 / 0:30</div>
</div>
<section class="welcome">
  <h1>WELCOME TO<br>BRIGHTPATH INTERNATIONAL</h1>
  <p>BrightPath INTERNATIONAL (BPI) is a not-for-profit organization that seeks to break the cycle of poverty by equipping and empowering children. We do this primarily through sponsorship which provides housing, food, medicine, and education. We also work in emergency relief and manage a scholarship fund for further education. Our current website is outdated in it’s look and we are wanting to update it’s appearance to have a more relevant esthetic and engaging user experience.</p>
</section>
<div class="abs btn btn-lg">VIEW MORE DETAILS</div>

<div class="abs section-title">RECENT POSTS</div>
<div class="abs pager"><span></span><span></span></div>
<article class="abs post" style="left:130px"><div class="post-img" role="img" aria-label="Photo of hands holding a seedling" style="background:linear-gradient(135deg,#3c2e1e,#b89a70)"></div><h3>REMINDED WHY WE DO THIS...</h3><small>Posted by Daniel Hale</small></article>
<article class="abs post" style="left:286px"><div class="post-img" role="img" aria-label="Photo of two boys outdoors" style="background:linear-gradient(135deg,#8d8a80,#3a4050)"></div><h3>REMINDED WHY WE DO THIS...</h3><small>Posted by Daniel Hale</small></article>
<article class="abs post" style="left:442px"><div class="post-img" role="img" aria-label="Photo of a child studying" style="background:linear-gradient(135deg,#2a2a2a,#a03030 60%,#2c4a9a)"></div><h3>REMINDED WHY WE DO THIS...</h3><small>Posted by Daniel Hale</small></article>
<article class="abs post" style="left:598px"><div class="post-img" role="img" aria-label="Photo of hands holding coins and a help sign" style="background:linear-gradient(135deg,#5a5a58,#c8c6c0)"></div><h3>REMINDED WHY WE DO THIS...</h3><small>Posted by Daniel Hale</small></article>

<div class="abs divider"></div>

<article class="abs card" style="left:130px"><div class="card-img" role="img" aria-label="Photo of two smiling boys" style="background:linear-gradient(135deg,#d8cdb8,#4a5f90)"></div><h3>PROGRAMS</h3><p>Unsponsored Children’s Fund ensures that registered children who have not yet been sponsored have their immediate</p><div class="btn">READ MORE</div></article>
<article class="abs card" style="left:338px"><div class="card-img" role="img" aria-label="Photo of a young man volunteer" style="background:linear-gradient(135deg,#4a6a9a,#3a2a22 50%,#c8c8d0)"></div><h3>GET INVOLVED</h3><p>Unsponsored Children’s Fund ensures that registered children who have not yet been sponsored have their immediate</p><div class="btn">READ MORE</div></article>
<article class="abs card" style="left:546px"><div class="card-img" role="img" aria-label="Photo of two young girls in white dresses" style="background:linear-gradient(135deg,#7a5a40,#e8e4de 55%,#5a3a2a)"></div><h3>WHERE WE WORK</h3><p>Unsponsored Children’s Fund ensures that registered children who have not yet been sponsored have their immediate</p><div class="btn">READ MORE</div></article>

<footer class="abs footer">
  Sponsor a Child &nbsp;|&nbsp; About Us &nbsp;|&nbsp; Where we Work &nbsp;|&nbsp; Programs &nbsp;|&nbsp; Get Involved &nbsp;|&nbsp; Donate &nbsp;|&nbsp; Blog &nbsp;|&nbsp; Contact<br>
  © 2015. BrightPath INTERNATIONAL’s. All Rights Reserved. &nbsp;|&nbsp; Terms of Service &nbsp;|&nbsp; Legal
</footer>
<div class="abs social">
  <span role="img" aria-label="Social link" style="background:var(--navy)"></span>
  <span role="img" aria-label="Social link" style="background:var(--blue-dark)"></span>
  <span role="img" aria-label="Social link" style="background:#3aa3dc"></span>
  <span role="img" aria-label="Social link" style="background:var(--red)"></span>
</div>
</body>
</html>
```